ご提案有難うございました。
最もサイトのトンマナにあっており、かつキャンペーンの売りが目立っていると感じたため、こちらのデザインを採用させて頂きました。
どれも素晴らしいご提案で御座いました。
また機会があればどうぞ宜しくお願い致します。
居酒屋予約 バナーデザイン バナー作成の仕事の依頼
希望する色 特になし・その他
バナーサイズ
• 300x250
目的・概要
居酒屋の割引キャンペーンページに誘導するために使用するバナー制作です。
依頼詳細
以下のページ等に設置致します。
https://www.pelmora-go.com/asia/japan/japa-japan/japa-restaurant/shinjuku-izakaya/
▽入れてほしい画像▽
会社ロゴ
▽入れてほしい文言▽
※以下の文章例を参考に、バナーデザインに映えるようご調整ください
■文章例
【最大100%割引】税込み2,160円以上の飲食で2,000円のキャッシュバックキャンペーン中!
【最大100%割引】居酒屋利用で2,000円のキャッシュバックキャンペーン中!
【最大100%割引】2,160円(税込)以上の居酒屋利用で2,000円の現金還元中!
Pelmora限定!居酒屋の利用で現金2,000円が貰える!
【最大100%割引】税込み2,160円の居酒屋利用で2,000円現金還元中!
Pelmora限定企画!税込み2,160円の居酒屋利用で2,000円現金還元中!!
3000店舗以上から選べる!税込み2,160円の居酒屋利用で2,000円現金還元中!!
居酒屋代金、実質最大100%オフ
3000店以上の居酒屋が実質最大100%割引
居酒屋の利用で漏れなく現金2,000円が貰える
▽バナーサイズ▽
▽納品形式▽
png/jpg
▽注意点・禁止事項▽
※他のクライアントへ既に提案した内容の転用など
※作成いただいたバナーに関して、納品後はクライアントに帰属します。
たくさんのウェブデザイナーの方からのご提案をお待ちしております!

```html
<!DOCTYPE html>
<html lang="ja">
<head>
<meta charset="utf-8">
<title>Pelmora 限定企画 居酒屋キャッシュバック バナー</title>
<link rel="stylesheet" href="https://fonts.googleapis.com/css2?family=Noto+Sans+JP:wght@700;900&display=swap">
<style>
  :root {
    --brand-blue-light: #45b0f2;
    --brand-blue-dark: #1877c9;
    --campaign-red-light: #d42a2a;
    --campaign-red-dark: #a40e12;
    --headline-red: #a8191c;
    --price-red: #c8161d;
    --text-ink: #1c1c1c;
    --marker-yellow: #ffe95a;
    --panel-white: rgba(255, 255, 255, 0.82);
    --white: #ffffff;
    --beer-light: #f3c46a;
    --beer-mid: #b8731f;
    --beer-dark: #3a1c08;
  }
  * { margin: 0; padding: 0; box-sizing: border-box; }
  html, body {
    width: 1200px;
    height: 1000px;
    overflow: hidden;
    background: var(--white);
  }
  .banner {
    position: relative;
    width: 1200px;
    height: 1000px;
    overflow: hidden;
    font-family: "Noto Sans JP", sans-serif;
  }
  .banner__photo {
    position: absolute;
    inset: 0;
    background:
      radial-gradient(ellipse at 45% 30%, rgba(255, 240, 200, 0.85) 0%, rgba(243, 196, 106, 0.6) 30%, transparent 60%),
      radial-gradient(ellipse at 80% 80%, var(--beer-light) 0%, transparent 55%),
      linear-gradient(160deg, var(--beer-dark) 0%, var(--beer-mid) 45%, var(--beer-light) 75%, var(--beer-mid) 100%);
  }
  .topbar {
    position: absolute;
    top: 0;
    left: 0;
    width: 1200px;
    height: 151px;
  }
  .topbar__shapes { position: absolute; inset: 0; }
  .brand {
    position: absolute;
    left: 40px;
    top: 0;
    height: 151px;
    display: flex;
    align-items: center;
    gap: 20px;
    color: var(--white);
    font-weight: 900;
    font-size: 64px;
    letter-spacing: 1px;
  }
  .brand__dot {
    width: 72px;
    height: 72px;
    border-radius: 50%;
    background: var(--white);
  }
  .campaign-tag {
    position: absolute;
    left: 760px;
    width: 400px;
    top: 0;
    height: 151px;
    display: flex;
    align-items: center;
    justify-content: center;
    color: var(--white);
    font-weight: 900;
    font-size: 68px;
    letter-spacing: 4px;
  }
  .offer-panel {
    position: absolute;
    left: 56px;
    top: 329px;
    width: 1089px;
    height: 504px;
    background: var(--panel-white);
    display: flex;
    flex-direction: column;
    align-items: center;
    padding-top: 22px;
  }
  .offer-panel__headline {
    color: var(--headline-red);
    font-weight: 900;
    font-size: 116px;
    line-height: 1.25;
    letter-spacing: 2px;
  }
  .offer-panel__condition {
    margin-top: 14px;
    color: var(--text-ink);
    font-weight: 900;
    font-size: 56px;
    line-height: 1.3;
  }
  .offer-panel__marker {
    background: linear-gradient(transparent 45%, var(--marker-yellow) 45%);
    padding: 0 4px;
  }
  .offer-panel__reward {
    margin-top: 10px;
    font-weight: 900;
    line-height: 1.3;
    white-space: nowrap;
  }
  .offer-panel__amount {
    color: var(--price-red);
    font-size: 84px;
  }
  .offer-panel__cashback {
    color: var(--headline-red);
    font-size: 74px;
    text-emphasis: filled dot var(--price-red);
    -webkit-text-emphasis: filled dot var(--price-red);
    text-emphasis-position: under;
    -webkit-text-emphasis-position: under;
  }
</style>
</head>
<body>
  <main class="banner">
    <div class="banner__photo" role="img" aria-label="居酒屋で生ビールのジョッキを掲げて乾杯する写真"></div>

    <header class="topbar">
      <svg class="topbar__shapes" width="1200" height="151" viewBox="0 0 1200 151" aria-hidden="true">
        <defs>
          <linearGradient id="campaignRed" x1="0" y1="0" x2="0" y2="1">
            <stop offset="0" stop-color="var(--campaign-red-light)"/>
            <stop offset="1" stop-color="var(--campaign-red-dark)"/>
          </linearGradient>
          <linearGradient id="brandBlue" x1="0" y1="0" x2="0" y2="1">
            <stop offset="0" stop-color="var(--brand-blue-light)"/>
            <stop offset="1" stop-color="var(--brand-blue-dark)"/>
          </linearGradient>
        </defs>
        <rect x="0" y="0" width="1200" height="151" fill="url(#campaignRed)"/>
        <polygon points="0,0 680,0 724,75.5 680,151 0,151" fill="var(--white)"/>
        <polygon points="0,0 664,0 708,75.5 664,151 0,151" fill="url(#brandBlue)"/>
      </svg>
      <div class="brand">
        <span class="brand__dot"></span>
        <span class="brand__name">Pelmora</span>
      </div>
      <div class="campaign-tag">限定企画！</div>
    </header>

    <section class="offer-panel">
      <h1 class="offer-panel__headline">最大100%割引</h1>
      <p class="offer-panel__condition">税込み<span class="offer-panel__marker">2,160円</span>の居酒屋利用で</p>
      <p class="offer-panel__reward"><span class="offer-panel__amount">2,000円</span><span class="offer-panel__cashback">現金還元中</span><span class="offer-panel__cashback-mark" style="color: var(--headline-red); font-size: 74px;">!!</span></p>
    </section>
  </main>
</body>
</html>
```